Lumen 7 auto detail

Looking for a flyer for my auto detail business
Hand Wash
• Clay Bar Application
• Machine Buff Wax / Compound /
Polish Paint Correction
• Clean Interior & Exterior Glass
• Vacuum, Shampoo, & Steam Clean
Upholstery, Carpets, Seats, Mats, & Trunk
• Pet Hair Removal
• Clean headliner
• Clean Doors/ Trunk/Hood Jambs
• Air Blow & Clean all Cracks & Crevices • Clean & Shine Protect All Vinyl/
Dash/Door Panels/Middle Console
Cleaning/Conditioning of Leather
• Clean, Treat, Dress, & Polish Tires,
Rims, & Wheel Wells
• Bug & Tar Removal
• Dress Black Exterior Plastic
• Minor Scratch Removal
• Engine Compartment Detail
Headlight Restoration (if needed)
• Interior Fragrance
• DRY ICE BLASTING
At Lumen 7 Auto Detail, we pride ourselves on providing a unique and exceptional experience that sets us apart from other detailers. Here are a few key factors that make us stand out:
1. Attention to Detail: We live up to our name by going above and beyond in every aspect of our car detailing services. Our team of skilled technicians pays meticulous attention to every nook and cranny of your vehicle, ensuring that it receives the highest level of care and precision.
2. Customized Solutions: We understand that each car is unique, and so are our clients' needs. That's why we offer personalized solutions tailored to your specific requirements. Whether you need a basic wash and wax or a comprehensive paint correction, we will work with you to create a customized detailing plan that meets your expectations.
3. Cutting-Edge Technology: We stay at the forefront of the industry by utilizing the latest tools, products, and techniques. Our team is trained in the most advanced detailing methods, allowing us to achieve superior results and deliver a finish that exceeds your expectations.
4. Exceptional Customer Service: We believe in providing not only exceptional car detailing but also an exceptional customer experience. Our friendly and knowledgeable staff is always ready to assist you, answer your questions, and ensure that you have a positive and enjoyable experience at our facility.
5. Eco-Friendly Practices: We are committed to reducing our environmental impact by using eco-friendly cleaning products and techniques. Our detailing processes are designed to minimize water usage and waste generation, making us a responsible choice for those who care about the planet.
These factors, combined with our passion for cars and dedication to excellence, make Lumen 7 Auto Detail the premier choice for discerning car owners who seek a truly exceptional detailing experience.
We offer mobile services as well
Address 742 Corliss Ave. S., Renton, WA 98061

```html
<!DOCTYPE html>
<html lang="en">
<head>
<meta charset="utf-8">
<title>Lumen 7 Auto Detail – Flyer</title>
<link rel="stylesheet" href="https://fonts.googleapis.com/css2?family=Montserrat:wght@400;500;600;700;800&family=Poppins:wght@400;500;600&display=swap">
<style>
  :root {
    --ink: #0d0e11;
    --panel: #17181c;
    --panel-edge: #2a2b31;
    --red: #d9232d;
    --red-dark: #8e1219;
    --white: #ffffff;
    --muted: #c9cacf;
    --grey: #8a8b92;
  }
  * { margin: 0; padding: 0; box-sizing: border-box; }
  html, body { width: 887px; height: 1200px; overflow: hidden; background: var(--ink); }
  .flyer {
    position: relative; width: 887px; height: 1200px; overflow: hidden;
    background: radial-gradient(ellipse at 70% 30%, #24252b 0%, var(--ink) 65%);
    font-family: "Poppins", sans-serif; color: var(--white);
  }
  .accent-swoosh { position: absolute; left: 0; top: 0; width: 887px; height: 260px; }
  .brand {
    position: absolute; left: 38px; top: 70px; width: 250px;
    display: flex; align-items: center; gap: 12px;
  }
  .brand-dot { width: 26px; height: 26px; border-radius: 50%; background: var(--red); flex: none; }
  .brand-name {
    font-family: "Montserrat", sans-serif; font-weight: 800; font-size: 27px;
    line-height: 1.05; text-transform: uppercase; color: var(--white);
  }
  .headline {
    position: absolute; left: 310px; top: 58px; width: 540px;
    font-family: "Montserrat", sans-serif; font-weight: 800; font-size: 37px;
    line-height: 1.12; text-transform: uppercase; letter-spacing: .3px;
  }
  .intro {
    position: absolute; left: 310px; top: 178px; width: 530px;
    font-size: 15.5px; line-height: 1.5; color: var(--muted);
  }
  .values {
    position: absolute; left: 30px; top: 282px; width: 827px;
    display: flex; justify-content: space-between;
  }
  .value { width: 150px; text-align: center; }
  .value-icon {
    width: 76px; height: 76px; margin: 0 auto 12px; border-radius: 50%;
    border: 3px solid var(--red); display: flex; align-items: center; justify-content: center;
    background: #1c1d22;
  }
  .value-icon svg { width: 38px; height: 38px; }
  .value-label {
    font-family: "Montserrat", sans-serif; font-weight: 600; font-size: 16px; line-height: 1.2;
  }
  .services {
    position: absolute; left: 28px; top: 452px; width: 831px; height: 380px;
    background: linear-gradient(180deg, var(--panel) 0%, #111215 100%);
    border-top: 3px solid var(--red); border-radius: 4px;
  }
  .service { position: absolute; display: flex; gap: 14px; }
  .service-photo {
    width: 70px; height: 70px; flex: none; border: 3px solid var(--red);
    background: linear-gradient(135deg, #3a3b42 0%, #15161a 100%);
  }
  .service-title {
    font-family: "Montserrat", sans-serif; font-weight: 700; font-size: 14px;
    text-transform: uppercase; color: var(--white); margin-bottom: 4px; line-height: 1.25;
  }
  .service ul { list-style: none; }
  .service li { font-size: 12px; line-height: 1.42; color: var(--muted); }
  .service li::before { content: "• "; color: var(--red); }
  .car-photo {
    position: absolute; left: 60px; top: 790px; width: 767px; height: 290px;
    background: radial-gradient(ellipse at 50% 60%, #3b3c44 0%, #1a1b20 55%, transparent 75%);
  }
  .mobile-banner {
    position: absolute; left: 210px; top: 1090px; width: 467px; height: 36px;
    background: var(--red); display: flex; align-items: center; justify-content: center;
    font-family: "Montserrat", sans-serif; font-weight: 700; font-size: 15px;
    letter-spacing: 1px; text-transform: uppercase;
    clip-path: polygon(4% 0, 96% 0, 100% 100%, 0 100%);
  }
  .contact {
    position: absolute; left: 0; top: 1136px; width: 887px; height: 64px;
    background: #0a0a0c; border-top: 2px solid var(--red-dark);
    display: flex; align-items: center; justify-content: center; gap: 38px;
    font-size: 14px; color: var(--muted);
  }
  .contact-item { display: flex; align-items: center; gap: 8px; }
  .contact-item svg { width: 18px; height: 18px; }
</style>
</head>
<body>
<main class="flyer">
  <svg class="accent-swoosh" viewBox="0 0 887 260" aria-hidden="true">
    <path d="M0 0 H330 C240 40 120 90 0 200 Z" fill="#1e1f24"/>
    <path d="M0 215 C110 110 230 45 360 0 H385 C250 55 120 125 0 240 Z" fill="var(--red)"/>
  </svg>

  <div class="brand">
    <span class="brand-dot"></span>
    <span class="brand-name">Lumen 7 Auto Detail</span>
  </div>

  <h1 class="headline">Passion for cars &amp; dedication to excellence</h1>
  <p class="intro">Make Lumen 7 Auto Detail the premier choice for discerning car owners who seek a truly exceptional detailing experience.</p>

  <section class="values">
    <div class="value">
      <div class="value-icon"><svg viewBox="0 0 24 24" fill="none" stroke="#fff" stroke-width="1.8"><circle cx="10.5" cy="10.5" r="6"/><path d="M15 15l5 5"/></svg></div>
      <div class="value-label">Attention<br>to Detail</div>
    </div>
    <div class="value">
      <div class="value-icon"><svg viewBox="0 0 24 24" fill="none" stroke="#fff" stroke-width="1.8"><circle cx="12" cy="12" r="3.5"/><path d="M12 2v3M12 19v3M2 12h3M19 12h3M4.9 4.9l2.1 2.1M17 17l2.1 2.1M4.9 19.1L7 17M17 7l2.1-2.1"/></svg></div>
      <div class="value-label">Customized<br>Solutions</div>
    </div>
    <div class="value">
      <div class="value-icon"><svg viewBox="0 0 24 24" fill="none" stroke="#fff" stroke-width="1.8"><rect x="6" y="6" width="12" height="12" rx="1.5"/><path d="M9 2v4M15 2v4M9 18v4M15 18v4M2 9h4M2 15h4M18 9h4M18 15h4"/></svg></div>
      <div class="value-label">Cutting-Edge<br>Technology</div>
    </div>
    <div class="value">
      <div class="value-icon"><svg viewBox="0 0 24 24" fill="none" stroke="#fff" stroke-width="1.8"><path d="M4 14v-2a8 8 0 0116 0v2"/><rect x="3" y="13" width="4" height="6" rx="1"/><rect x="17" y="13" width="4" height="6" rx="1"/></svg></div>
      <div class="value-label">Exceptional<br>Customer Service</div>
    </div>
    <div class="value">
      <div class="value-icon"><svg viewBox="0 0 24 24" fill="none" stroke="#fff" stroke-width="1.8"><path d="M5 19C5 10 11 5 20 4c0 9-5 15-13 15"/><path d="M5 19l8-8"/></svg></div>
      <div class="value-label">Eco-Friendly<br>Practices</div>
    </div>
  </section>

  <section class="services">
    <div class="service" style="left:22px; top:22px; width:390px;">
      <div class="service-photo" role="img" aria-label="Photo of a car being hand washed"></div>
      <div>
        <h2 class="service-title">Hand Wash</h2>
        <ul>
          <li>Clay Bar Application</li>
          <li>Machine Buff Wax / Compound / Polish Paint Correction</li>
          <li>Clean Interior &amp; Exterior Glass</li>
          <li>Vacuum, Shampoo, &amp; Steam Clean</li>
        </ul>
      </div>
    </div>
    <div class="service" style="left:22px; top:152px; width:390px;">
      <div class="service-photo" role="img" aria-label="Photo of a polished car wheel"></div>
      <div>
        <h2 class="service-title">Rims, &amp; Wheel Wells</h2>
        <ul>
          <li>Bug &amp; Tar Removal</li>
          <li>Dress Black Exterior Plastic</li>
          <li>Minor Scratch Removal</li>
          <li>Engine Compartment Detail</li>
        </ul>
      </div>
    </div>
    <div class="service" style="left:22px; top:280px; width:390px;">
      <div class="service-photo" role="img" aria-label="Photo of a restored car headlight"></div>
      <div>
        <h2 class="service-title">Headlight Restoration (if needed)</h2>
        <ul>
          <li>Interior Fragrance</li>
          <li>Dry Ice Blasting</li>
        </ul>
      </div>
    </div>
    <div class="service" style="left:432px; top:22px; width:380px;">
      <div class="service-photo" role="img" aria-label="Photo of a clean car dashboard"></div>
      <div>
        <h2 class="service-title">Dash/Door Panels/Middle Console Cleaning/Conditioning of Leather</h2>
        <ul>
          <li>Clean, Treat, Dress, &amp; Polish Tires</li>
        </ul>
      </div>
    </div>
    <div class="service" style="left:432px; top:152px; width:380px;">
      <div class="service-photo" role="img" aria-label="Photo of clean car seats"></div>
      <div>
        <h2 class="service-title">Upholstery, Carpets, Seats, Mats, &amp; Trunk</h2>
        <ul>
          <li>Pet Hair Removal</li>
          <li>Clean Headliner</li>
          <li>Clean Doors/ Trunk/Hood Jambs</li>
          <li>Air Blow &amp; Clean all Cracks &amp; Crevices</li>
          <li>Clean &amp; Shine Protect All Vinyl</li>
        </ul>
      </div>
    </div>
  </section>

  <div class="car-photo" role="img" aria-label="Photo of a glossy black sedan being polished by a detailer"></div>

  <div class="mobile-banner">We offer mobile services as well</div>

  <footer class="contact">
    <span class="contact-item"><svg viewBox="0 0 24 24" fill="var(--red)"><path d="M12 2a7 7 0 00-7 7c0 5 7 13 7 13s7-8 7-13a7 7 0 00-7-7zm0 9.5A2.5 2.5 0 1112 6.5a2.5 2.5 0 010 5z"/></svg>742 Corliss Ave. S., Renton, WA 98061</span>
    <span class="contact-item"><svg viewBox="0 0 24 24" fill="var(--red)"><path d="M6.6 10.8a15 15 0 006.6 6.6l2.2-2.2a1 1 0 011-.25 11 11 0 003.6.6 1 1 0 011 1V20a1 1 0 01-1 1A17 17 0 013 4a1 1 0 011-1h3.5a1 1 0 011 1 11 11 0 00.6 3.6 1 1 0 01-.25 1z"/></svg>555 201 4477</span>
    <span class="contact-item"><svg viewBox="0 0 24 24" fill="none" stroke="var(--red)" stroke-width="2"><circle cx="12" cy="12" r="9"/><path d="M3 12h18M12 3c3 3 3 15 0 18M12 3c-3 3-3 15 0 18"/></svg>lumen7autodetail.example</span>
  </footer>
</main>
</body>
</html>
```